Life and Personal development life coach needs card design

I need a card design that matches the style and design of my website. I'd like to stay in the same color scheme. Please check out my website for ideas. www.bretamoorvale.com
I have had previous designs for this. I am wondering if you have access to those for more ideas??

```html
<!DOCTYPE html>
<html lang="en">
<head>
<meta charset="utf-8">
<title>Breta Moorvale – Business Card</title>
<link rel="stylesheet" href="https://fonts.googleapis.com/css2?family=Barlow:wght@300;400;500;600&display=swap">
<style>
  :root {
    --stage: #595755;
    --card-top: #ffffff;
    --card-bottom: #e4e4e4;
    --green: #5aad33;
    --green-dark: #3f8d2e;
    --green-light: #8cc63f;
    --green-text: #6cb93a;
    --fold-gray: #c9c9c9;
    --fold-gray-light: #ececec;
    --white: #ffffff;
    --photo-a: #c9bfae;
    --photo-b: #2f3a5a;
  }
  html, body {
    margin: 0;
    padding: 0;
    width: 926px;
    height: 1200px;
    overflow: hidden;
    background: var(--stage);
  }
  .stage { display: block; width: 926px; height: 1200px; }
  .type { font-family: "Barlow", Arial, sans-serif; }
  .band { fill: url(#bandGrad); }
  .band-dark { fill: var(--green-dark); }
  .fold-gray { fill: url(#foldGrad); }
  .card-face { fill: url(#cardGrad); }
  .stripe-gap { stroke: var(--white); stroke-width: 4; }
  .name { font-size: 33px; font-weight: 600; fill: var(--white); }
  .role { font-size: 15px; font-weight: 400; fill: var(--white); }
  .hook-strong { font-size: 22px; font-weight: 600; fill: var(--white); letter-spacing: -0.5px; }
  .hook-light { font-size: 17px; font-weight: 300; fill: var(--white); letter-spacing: 1px; }
  .values { font-size: 16px; font-weight: 400; fill: var(--green-text); }
  .contact { font-size: 16px; font-weight: 400; fill: var(--green-text); }
  .icon-tab { fill: var(--green); }
  .icon-line { fill: none; stroke: var(--white); stroke-width: 1.4; }
  .icon-fill { fill: var(--white); }
  .site { font-size: 19px; font-weight: 600; fill: var(--white); letter-spacing: 3px; }
  .tagline-strong { font-size: 41px; font-weight: 600; fill: var(--green-light); letter-spacing: -1.5px; }
  .tagline-light { font-size: 30px; font-weight: 300; fill: var(--green-light); letter-spacing: 1.5px; }
</style>
</head>
<body>
<svg class="stage" viewBox="0 0 903 1170" xmlns="http://www.w3.org/2000/svg">
  <defs>
    <linearGradient id="bandGrad" x1="0" y1="0" x2="1" y2="0">
      <stop offset="0" stop-color="#3f8d2e"/>
      <stop offset="0.5" stop-color="#6bb934"/>
      <stop offset="1" stop-color="#8cc63f"/>
    </linearGradient>
    <linearGradient id="foldGrad" x1="0" y1="0" x2="1" y2="0">
      <stop offset="0" stop-color="#bdbdbd"/>
      <stop offset="1" stop-color="#ececec"/>
    </linearGradient>
    <linearGradient id="cardGrad" x1="0" y1="0" x2="0" y2="1">
      <stop offset="0" stop-color="#f4f4f4"/>
      <stop offset="1" stop-color="#e2e2e2"/>
    </linearGradient>
    <linearGradient id="photoGrad" x1="0" y1="0" x2="1" y2="1">
      <stop offset="0" stop-color="#d8cdb8"/>
      <stop offset="0.55" stop-color="#5a6078"/>
      <stop offset="1" stop-color="#1f2740"/>
    </linearGradient>
  </defs>

  <!-- FRONT -->
  <g class="card card-front">
    <rect class="card-face" x="88" y="140" width="732" height="428"/>

    <!-- left header band -->
    <rect class="band" x="88" y="189" width="160" height="109"/>
    <polygon class="band-dark" points="248,189 323,153 323,264 248,298"/>
    <rect class="band" x="323" y="153" width="497" height="111"/>

    <!-- stripes under header -->
    <rect class="band" x="88" y="303" width="160" height="9"/>
    <line class="stripe-gap" x1="96" y1="301" x2="100" y2="314"/>
    <line class="stripe-gap" x1="222" y1="301" x2="226" y2="314"/>
    <polygon class="band-dark" points="248,303 323,269 323,278 248,312"/>
    <rect class="band" x="323" y="269" width="497" height="9"/>
    <line class="stripe-gap" x1="354" y1="267" x2="358" y2="280"/>
    <line class="stripe-gap" x1="482" y1="267" x2="486" y2="280"/>
    <line class="stripe-gap" x1="610" y1="267" x2="614" y2="280"/>
    <line class="stripe-gap" x1="740" y1="267" x2="744" y2="280"/>

    <!-- gray fold -->
    <polygon class="fold-gray" points="248,316 323,282 323,502 248,536"/>

    <!-- bottom bands -->
    <rect class="band" x="88" y="536" width="160" height="17"/>
    <polygon class="band-dark" points="248,536 323,502 323,520 248,553"/>
    <rect class="band" x="323" y="502" width="497" height="18"/>

    <!-- header text -->
    <text class="type hook-strong" x="234" y="219" text-anchor="end">Discover</text>
    <text class="type hook-strong" x="234" y="242" text-anchor="end">what is</text>
    <text class="type hook-light" x="234" y="263" text-anchor="end">possible</text>
    <text class="type hook-light" x="234" y="280" text-anchor="end">today!</text>

    <text class="type name" x="370" y="208">BRETA MOORVALE, RN</text>
    <text class="type role" x="349" y="229">Transformation and Personal Development Life Coach</text>

    <text class="type values" x="234" y="438" text-anchor="end">Health,</text>
    <text class="type values" x="234" y="459" text-anchor="end">Strength</text>
    <text class="type values" x="234" y="480" text-anchor="end">&amp; Balance for</text>
    <text class="type values" x="234" y="501" text-anchor="end">Your Mind</text>
    <text class="type values" x="234" y="522" text-anchor="end">and Soul</text>

    <!-- portrait area -->
    <rect x="645" y="291" width="175" height="198" fill="url(#photoGrad)" role="img" aria-label="Portrait photo of the coach"/>

    <!-- contact rows -->
    <text class="type contact" x="587" y="397" text-anchor="end">555-013-2847</text>
    <rect class="icon-tab" x="594" y="380" width="46" height="22"/>
    <path class="icon-fill" d="M599 386 q8 -4 16 0 l0 3 -4 0 0 -2 q-4 -1 -8 0 l0 2 -4 0z M602 390 h10 l2 7 h-14z"/>

    <text class="type contact" x="587" y="425" text-anchor="end">@bretamoor</text>
    <rect class="icon-tab" x="594" y="408" width="46" height="22"/>

    <text class="type contact" x="587" y="453" text-anchor="end">Breta Moorvale</text>
    <rect class="icon-tab" x="594" y="436" width="46" height="22"/>

    <text class="type contact" x="587" y="481" text-anchor="end">breta@bretamoorvale.com</text>
    <rect class="icon-tab" x="594" y="464" width="46" height="24"/>
    <rect class="icon-line" x="598" y="470" width="16" height="12"/>
    <polyline class="icon-line" points="598,470 606,477 614,470"/>
  </g>

  <!-- BACK -->
  <g class="card card-back">
    <rect class="card-face" x="88" y="601" width="732" height="429"/>

    <rect class="band" x="88" y="701" width="84" height="39"/>
    <rect class="band" x="735" y="701" width="85" height="39"/>
    <polygon class="band-dark" points="172,701 212,720 212,760 172,740"/>
    <polygon class="band-dark" points="735,701 696,720 696,760 735,740"/>
    <rect class="band" x="212" y="720" width="484" height="40"/>

    <polygon class="fold-gray" points="172,740 212,760 212,910 172,890"/>
    <polygon class="fold-gray" points="735,740 696,760 696,910 735,890" transform="translate(1431 0) scale(-1 1)" opacity="0"/>
    <polygon fill="#d4d4d4" points="735,740 696,760 696,910 735,890"/>

    <rect class="band" x="88" y="890" width="84" height="20"/>
    <rect class="band" x="735" y="890" width="85" height="20"/>
    <polygon class="band-dark" points="172,890 212,910 212,930 172,910"/>
    <polygon class="band-dark" points="735,890 696,910 696,930 735,910"/>
    <rect class="band" x="212" y="910" width="484" height="20"/>

    <text class="type site" x="454" y="746" text-anchor="middle">www.bretamoorvale.com</text>
    <text class="type tagline-strong" x="454" y="828" text-anchor="middle">Discover what is</text>
    <text class="type tagline-light" x="454" y="866" text-anchor="middle">possible today!</text>
  </g>
</svg>
</body>
</html>
```